Computer Repair Shop needs bold business card

An established computer repair shop with a new owner wants a business card that is his own. Keeping with the tradition of the shop the card should be clever with a bold background colour(s). We want to portray a sense of continuity from the last branding because the only thing that changed is the owner. Reliable services, quality parts, fast, friendly, helpful, affordable are still the same and key to the business philosophy.

Target Market(s)

Personal and business computer owners

Industry/Entity Type

Computer Repair

Contact Information for Business Card

please see the file for address details for the card. Card should read Tomas Varga and owner as well.

Font styles to use
Serif
Sans Serif

Colors
fbed22
ffc214
f78f20
f37122
ffffff

Requirements
Must have
• Bold background colours with a tech influence, clear fonts. I added a copy of a PDF flyer we made quickly in the files. It contains the specific details and the colours and style we prefer. The image is from www.pixelmeadowart.com .... not sure if we should be using it for business so we might need to change that but something along those lines is where to start.
Nice to have
• We don't have a logo yet so the name in text with an awesome background is required for now to get our branding process going in the right direction. A map on the back would be nice can be google copy or drawn but must reference court house and library landmarks. "Absolute Satisfaction Guaranteed"
Should not have
• a boring picture of a computer or laptop

```html
<!DOCTYPE html>
<html lang="en">
<head>
<meta charset="utf-8">
<title>Steadfast Computer – Business Card</title>
<link rel="stylesheet" href="https://fonts.googleapis.com/css2?family=Oswald:wght@700&family=Roboto:wght@400;500&display=swap">
<style>
  :root {
    --bg: #e4e4e4;
    --yellow: #fbed22;
    --gold: #ffc214;
    --orange: #f78f20;
    --deep-orange: #f37122;
    --band-orange: #e8620e;
    --red: #e02a1e;
    --ink: #1a1a1a;
    --ink-soft: #3a2a10;
    --white: #ffffff;
  }
  * { margin: 0; padding: 0; box-sizing: border-box; }
  html, body { width: 1200px; height: 1200px; overflow: hidden; }
  body {
    background: var(--bg);
    font-family: "Roboto", sans-serif;
    position: relative;
  }
  .card {
    position: absolute;
    left: 220px;
    width: 760px;
    height: 434px;
    border-radius: 22px;
    overflow: hidden;
    background: radial-gradient(ellipse at 45% 35%, var(--yellow) 0%, var(--gold) 30%, var(--orange) 70%, var(--deep-orange) 100%);
    box-shadow: 0 6px 18px rgba(0,0,0,0.18);
  }
  .card--front { top: 130px; }
  .card--back { top: 636px; }

  .network-texture {
    position: absolute;
    background: radial-gradient(ellipse at center, rgba(255,240,180,0.35) 0%, rgba(255,240,180,0) 70%);
  }
  .card--front .network-texture { right: 0; top: 60px; width: 460px; height: 320px; }
  .card--back .network-texture { left: 60px; top: 0; width: 700px; height: 260px; }

  .company-name {
    font-family: "Oswald", sans-serif;
    font-weight: 700;
    color: var(--ink);
    text-transform: uppercase;
    letter-spacing: 1px;
    position: absolute;
  }
  .card--front .company-name {
    left: 0; right: 0; top: 180px;
    text-align: center;
    font-size: 62px;
  }
  .card--back .company-name {
    left: 110px; top: 190px;
    font-size: 50px;
    line-height: 1.05;
  }

  .contact {
    position: absolute;
    left: 440px; top: 108px;
    color: var(--ink);
  }
  .contact__name {
    font-family: "Oswald", sans-serif;
    font-weight: 700;
    font-size: 24px;
    text-transform: uppercase;
    letter-spacing: 0.5px;
  }
  .contact__title {
    font-size: 15px;
    color: var(--ink-soft);
    margin: 2px 0 16px 8px;
  }
  .contact__list { list-style: none; font-size: 14px; }
  .contact__list li { display: flex; align-items: center; gap: 8px; height: 24px; }
  .contact__icon { width: 16px; height: 16px; flex: none; }
  .contact__list .no-icon { padding-left: 24px; }

  .card__footer { position: absolute; left: 0; bottom: 0; width: 760px; height: 110px; }
  .website {
    position: absolute;
    right: 36px; bottom: 36px;
    color: var(--white);
    font-size: 18px;
    letter-spacing: 0.3px;
  }
</style>
</head>
<body>

  <section class="card card--front" aria-label="Card front">
    <div class="network-texture" role="img" aria-label="Faint connected-node network pattern"></div>
    <h1 class="company-name">Steadfast Computer</h1>
  </section>

  <section class="card card--back" aria-label="Card back">
    <div class="network-texture" role="img" aria-label="Faint connected-node network pattern"></div>
    <h2 class="company-name">Steadfast<br>Computer</h2>

    <div class="contact">
      <p class="contact__name">Your Name</p>
      <p class="contact__title">Your Title</p>
      <ul class="contact__list">
        <li>
          <svg class="contact__icon" viewBox="0 0 16 16" aria-hidden="true">
            <path d="M2 6 Q8 1 14 6 L12 8 L10 6 Q8 5 6 6 L4 8 Z" fill="var(--ink)"/>
            <rect x="4" y="8" width="8" height="6" rx="1" fill="var(--ink)"/>
          </svg>
          <span>555 010 20405</span>
        </li>
        <li>
          <svg class="contact__icon" viewBox="0 0 16 16" aria-hidden="true">
            <rect x="1" y="3" width="14" height="10" fill="var(--ink)"/>
            <path d="M1 3 L8 9 L15 3" stroke="var(--gold)" stroke-width="1.3" fill="none"/>
          </svg>
          <span>yourname@steadfastcomputer.com</span>
        </li>
        <li class="no-icon"><span>212, 3150 Elm Street Lakeview AB</span></li>
      </ul>
    </div>

    <svg class="card__footer" viewBox="0 0 760 110" aria-hidden="true">
      <defs>
        <linearGradient id="bandGrad" x1="0" x2="1" y1="0" y2="0">
          <stop offset="0" stop-color="var(--band-orange)"/>
          <stop offset="0.75" stop-color="var(--deep-orange)"/>
          <stop offset="1" stop-color="var(--red)"/>
        </linearGradient>
      </defs>
      <polygon points="700,0 760,0 760,40 700,40" fill="var(--red)"/>
      <polygon points="450,40 760,40 760,110 470,110" fill="url(#bandGrad)"/>
      <polygon points="0,80 490,80 470,110 0,110" fill="var(--ink)"/>
    </svg>
    <p class="website">www.steadfastcomputer.com</p>
  </section>

</body>
</html>
```